Poster: Meditation course

We would like a simple poster to advertise a 10-day meditation course. We would like something very simple and minimal, nothing fancy. We will be putting this poster up around our local area and leaving it on cafe tables etc. We will also be sending it around digitally.
The poster should include the words below. (Please note that we may want to change these words further along in the process.) And in terms of imagery, something like a lotus flower could work well. (Please see the attached lotus flower and lily image in our newsletters, although it doesn't need to be that old school.) The size can be US Letter size / Europe A4. Please include the attached QR code, and please note that for the digital version we would like hyperlinks for the webpage and email. Many thanks!
Text for the poster:
Meditation produces a calm mind
10-day residential meditation course
Willow Cove, Northshore
7-17th June 2024
Vipassana meditation in the Theravada Buddhism tradition as taught by Tharamin U Lo Pwint and Mother Dawkelanyi
To apply: https://www.quietriverretreathouse.org/
For more information contact: info@quietriverretreathouse.org
Target Market(s)
Primarily university students. Also other people in California
Look and feel
Each slider illustrates characteristics of the customer's brand and the style your logo design should communicate.

```html
<!DOCTYPE html>
<html lang="en">
<head>
<meta charset="utf-8">
<title>Meditation Course Poster</title>
<link rel="stylesheet" href="https://fonts.googleapis.com/css2?family=DM+Serif+Display&family=Poppins:wght@300;400;500;600;700;800&display=swap">
<style>
  :root {
    --page-bg: #f4f3f1;
    --purple-top: #2c0f63;
    --purple-mid: #1f0a4a;
    --purple-bottom: #100526;
    --band: #2a1a68;
    --green: #3f9b2c;
    --green-light: #4caf35;
    --white: #ffffff;
    --title-tint: #dfe9f7;
    --muted: #d9d3ea;
    --pill-border: #6a3bb0;
    --pill-fill: rgba(20, 6, 50, 0.6);
    --pin: #e0243a;
  }
  * { margin: 0; padding: 0; box-sizing: border-box; }
  html, body { width: 1200px; height: 2906px; overflow: hidden; background: var(--page-bg); }
  .canvas { position: relative; width: 1200px; height: 2906px; }
  .poster {
    position: absolute; left: 109px; top: 818px;
    width: 982px; height: 1270px;
    background: linear-gradient(180deg, var(--purple-top) 0%, var(--purple-mid) 55%, var(--purple-bottom) 100%);
    overflow: hidden;
    font-family: "Poppins", sans-serif; color: var(--white);
    transform: scale(1.12); transform-origin: center center;
  }
  .hero-art {
    position: absolute; left: 0; top: 120px; width: 982px; height: 560px;
    background:
      radial-gradient(ellipse 260px 200px at 50% 48%, rgba(255,220,255,0.9) 0%, rgba(214,90,240,0.7) 35%, rgba(120,40,200,0.35) 65%, rgba(40,14,100,0) 100%),
      radial-gradient(ellipse 480px 260px at 50% 70%, rgba(170,50,220,0.55) 0%, rgba(60,20,130,0) 100%);
  }
  .hero-art::after {
    content: ""; position: absolute; left: 0; right: 0; bottom: 0; height: 140px;
    background: linear-gradient(180deg, rgba(31,10,74,0) 0%, var(--purple-mid) 100%);
  }
  .title {
    position: absolute; left: 0; width: 100%; top: 72px; text-align: center;
    font-family: "DM Serif Display", serif; font-weight: 400; font-size: 150px; line-height: 1;
    color: var(--title-tint); letter-spacing: -3px;
  }
  .tagline {
    position: absolute; left: 0; width: 100%; top: 248px; text-align: center;
    font-size: 42px; font-weight: 500; letter-spacing: 6px;
  }
  .course {
    position: absolute; left: 60px; top: 668px; height: 96px; display: flex; align-items: center;
  }
  .course-number { font-size: 112px; font-weight: 800; letter-spacing: -6px; line-height: 1; margin-right: -6px; position: relative; z-index: 1; }
  .course-day {
    background: var(--green); height: 68px; padding: 0 12px; display: flex; align-items: center;
    font-size: 42px; font-weight: 700;
  }
  .course-name {
    background: var(--band); height: 68px; width: 620px; display: flex; align-items: center; padding-left: 10px;
    font-size: 35px; font-weight: 400; letter-spacing: 0.5px; white-space: nowrap;
  }
  .dates {
    position: absolute; left: 0; width: 100%; top: 780px;
    font-size: 78px; font-weight: 700; line-height: 1; letter-spacing: -1px;
    display: flex; justify-content: center; align-items: flex-start;
  }
  .dates sup { font-size: 26px; font-weight: 600; margin-top: 4px; margin-right: 4px; }
  .dates .to {
    display: inline-flex; width: 26px; height: 26px; border-radius: 50%; background: var(--green);
    font-size: 11px; font-weight: 700; align-items: center; justify-content: center; margin: 38px 8px 0 0; letter-spacing: 0;
  }
  .dates .month { margin-left: 8px; }
  .dates .year { color: var(--green-light); font-weight: 400; margin-left: 14px; }
  .location {
    position: absolute; left: 50%; top: 894px; transform: translateX(-50%); height: 50px;
    border: 2px solid var(--pill-border); border-radius: 26px; background: var(--pill-fill);
    display: flex; align-items: center; padding: 0 30px 0 22px; gap: 20px;
    font-size: 27px; font-weight: 400; white-space: nowrap;
  }
  .tradition-title {
    position: absolute; left: 0; width: 100%; top: 975px; text-align: center;
    font-family: "DM Serif Display", serif; font-weight: 400; font-size: 48px; letter-spacing: -1px;
  }
  .tradition-text {
    position: absolute; left: 120px; width: 742px; top: 1044px; text-align: center;
    font-size: 24px; font-weight: 300; line-height: 1.25; color: var(--muted);
  }
  .contact { position: absolute; top: 1136px; }
  .contact-apply { left: 88px; }
  .contact-info { left: 532px; }
  .contact-label {
    display: inline-block; background: var(--green); border-radius: 4px; padding: 3px 12px;
    font-size: 17px; font-weight: 600;
  }
  .contact-info .contact-label { font-weight: 400; }
  .contact-link { display: block; margin-top: 8px; color: var(--white); text-decoration: none; font-size: 19px; font-weight: 400; white-space: nowrap; }
</style>
</head>
<body>
<div class="canvas">
  <section class="poster">
    <div class="hero-art" role="img" aria-label="Three silhouetted people meditating cross-legged in front of a glowing purple lotus flower with a faint mandala pattern"></div>
    <h1 class="title">Meditation</h1>
    <p class="tagline">PRODUCES A CALM MIND</p>

    <div class="course">
      <span class="course-number">10</span>
      <span class="course-day">DAY</span>
      <span class="course-name">RESIDENTIAL MEDITATION COURSE</span>
    </div>

    <div class="dates">
      <span>7</span><sup>TH</sup>
      <span class="to">TO</span>
      <span>17</span><sup>TH</sup>
      <span class="month">JUNE</span>
      <span class="year">2024</span>
    </div>

    <div class="location">
      <svg width="18" height="26" viewBox="0 0 18 26" aria-hidden="true">
        <path d="M9 0C4 0 0 4 0 9c0 6.5 9 17 9 17s9-10.5 9-17C18 4 14 0 9 0z" fill="var(--pin)"/>
        <circle cx="9" cy="9" r="3.5" fill="#fff"/>
      </svg>
      <span>Willow Cove, Northshore</span>
    </div>

    <h2 class="tradition-title">VIPASSANA MEDITATION</h2>
    <p class="tradition-text">in the Theravada Buddhism tradition as taught by Tharamin U Lo Pwint and Mother Dawkelanyi</p>

    <div class="contact contact-apply">
      <span class="contact-label">TO APPLY</span>
      <a class="contact-link" href="https://www.quietriverretreathouse.org/">www.quietriverretreathouse.org</a>
    </div>
    <div class="contact contact-info">
      <span class="contact-label">For more information contact</span>
      <a class="contact-link" href="mailto:info@quietriverretreathouse.org">info@quietriverretreathouse.org</a>
    </div>
  </section>
</div>
</body>
</html>
```